beauty salon application for consumer

- Find your favorite beauty salons and spas or discover new places next to you with geolocation;
- Filter your search by price, distance, category and type of service;
- Never worry again about having to schedule during your work hours or about not having your calls answered when you want to book an appointment;
- Mark salons as favorites and be the first to be informed of exclusive discounts;
- Don’t ever forget your appointments with Glow Nook’s notifications;
- Compare prices, places and services freely, in a quick and practical way;
- Share reviews about services and places you go with other users and read their opinions;
- USER-FRIENDLY INTERFACE
- GALLERY
- OFFERS

similar interface with application name "primlane"

Industry/Entity Type

Beauty Salon

Font styles to use
Decorative
Script

Colors

Designer to choose colors to be used in the design.

Requirements
Must have
• Please have a look into these applications:
• 1- https://apps.example-store.test/gb/app/primlane/id502918377/?pid=corvella&c=footer-link
• 2- https://apps.example-store.test/us/app/fizz-ltd-book-curl-set-glam-nail-services/id6093817245
• 3- https://market.sample-apps.test/store/apps/details?id=com.lumiparlour.user&hl=en
• 4- https://apps.example-store.test/app/id361720498?mt=8
Nice to have
• Nice to give me a clear screenshots for main function of the application ,please see the above applications before giving me a design .

```html
<!DOCTYPE html>
<html lang="en">
<head>
<meta charset="utf-8">
<title>lumelle – app screens</title>
<link rel="stylesheet" href="https://fonts.googleapis.com/css2?family=Dosis:wght@400;500;600&display=swap">
<style>
  :root {
    --backdrop: #6f6880;
    --ink: #4f4e66;
    --header: #514f66;
    --white: #ffffff;
    --divider: #ece4e4;
    --photo-top: #f7cfca;
    --photo-mid: #f6c2bc;
    --photo-bottom: #f9d6d1;
    --form-top: #f9cdc8;
    --form-bottom: #f4aa9f;
    --field-line: rgba(255, 255, 255, 0.55);
  }
  * { box-sizing: border-box; margin: 0; padding: 0; }
  html, body {
    width: 1200px;
    height: 1000px;
    overflow: hidden;
  }
  body {
    position: relative;
    background: var(--backdrop);
    font-family: "Dosis", sans-serif;
    color: var(--ink);
  }
  .screen {
    position: absolute;
    top: 200px;
    width: 338px;
    height: 602px;
    overflow: hidden;
    background: var(--white);
  }
  .screen--welcome { left: 180px; }
  .screen--signup { left: 682px; }

  /* Welcome screen */
  .hero-photo {
    position: absolute;
    left: 0; top: 0;
    width: 100%;
    height: 477px;
    background: radial-gradient(ellipse at 50% 35%, #fbe3df 0%, var(--photo-mid) 55%, var(--photo-top) 100%),
                linear-gradient(var(--photo-top), var(--photo-bottom));
  }
  .brand-name {
    position: absolute;
    left: 0; right: 0;
    font-weight: 500;
    text-align: center;
    letter-spacing: 0.5px;
  }
  .screen--welcome .brand-name {
    top: 356px;
    font-size: 50px;
    color: var(--ink);
  }
  .tagline {
    position: absolute;
    left: 0; right: 0;
    top: 430px;
    text-align: center;
    font-size: 14px;
    color: var(--ink);
  }
  .action {
    position: absolute;
    left: 0; right: 0;
    height: 62px;
    display: flex;
    align-items: center;
    justify-content: center;
    background: var(--white);
    font-size: 19px;
    font-weight: 500;
    letter-spacing: 1.2px;
    color: var(--ink);
  }
  .action--login { top: 477px; border-bottom: 1px solid var(--divider); }
  .action--create { top: 540px; }

  /* Sign-up screen */
  .app-header {
    position: absolute;
    left: 0; top: 0;
    width: 100%;
    height: 108px;
    background: var(--header);
  }
  .screen--signup .brand-name {
    top: 36px;
    font-size: 34px;
    color: var(--white);
  }
  .signup-form {
    position: absolute;
    left: 0; top: 108px;
    width: 100%;
    height: 432px;
    background: linear-gradient(var(--form-top), var(--form-bottom));
  }
  .add-user-icon {
    position: absolute;
    left: 146px; top: 36px;
  }
  .field {
    position: absolute;
    left: 28px;
    width: 284px;
    height: 40px;
    border-bottom: 1px solid var(--field-line);
    display: flex;
    align-items: center;
    justify-content: space-between;
    color: var(--white);
    font-size: 14px;
    letter-spacing: 1.6px;
  }
  .field svg { margin-right: 2px; }
  .field--name { top: 144px; }
  .field--email { top: 199px; }
  .field--password { top: 254px; }
  .field--birthday { top: 308px; }
  .screen--signup .action--create { top: 540px; }
</style>
</head>
<body>

<section class="screen screen--welcome">
  <div class="hero-photo" role="img" aria-label="Portrait photo of a smiling woman with long wavy hair, washed in soft pink"></div>
  <div class="brand-name">lumelle</div>
  <p class="tagline">discover and book beauty appointments</p>
  <div class="action action--login">LOGIN</div>
  <div class="action action--create">CREATE ACCOUNT</div>
</section>

<section class="screen screen--signup">
  <header class="app-header">
    <div class="brand-name">lumelle</div>
  </header>
  <form class="signup-form">
    <svg class="add-user-icon" width="66" height="66" viewBox="0 0 66 66" fill="none" stroke="#fff" stroke-width="2" stroke-linecap="round">
      <circle cx="24" cy="38" r="20"/>
      <circle cx="24" cy="33" r="6.5"/>
      <path d="M12 52 c3-8 21-8 24 0"/>
      <path d="M50 4 v18 M41 13 h18"/>
    </svg>
    <label class="field field--name">FULL NAME
      <svg width="20" height="10" viewBox="0 0 20 10" stroke="#fff" stroke-width="1.6" stroke-linecap="round"><path d="M6 2 h13 M1 8 h18"/></svg>
    </label>
    <label class="field field--email">EMAIL
      <svg width="20" height="16" viewBox="0 0 20 16" fill="none" stroke="#fff" stroke-width="1.6" stroke-linejoin="round"><rect x="1" y="1" width="18" height="14" rx="1"/><path d="M1 2 l9 7 l9-7"/></svg>
    </label>
    <label class="field field--password">PASSWORD
      <svg width="18" height="20" viewBox="0 0 18 20" fill="none" stroke="#fff" stroke-width="1.6"><rect x="1" y="8" width="16" height="11" rx="1"/><path d="M5 8 V5 a4 4 0 0 1 8 0 V8"/><circle cx="9" cy="13.5" r="1.5"/></svg>
    </label>
    <label class="field field--birthday">BIRTHDAY
      <svg width="20" height="20" viewBox="0 0 20 20" fill="none" stroke="#fff" stroke-width="1.6" stroke-linejoin="round"><rect x="2" y="9" width="16" height="10"/><rect x="1" y="5" width="18" height="4"/><path d="M10 5 v14"/><path d="M10 5 c-2-4-6-4-5-1 M10 5 c2-4 6-4 5-1"/></svg>
    </label>
  </form>
  <div class="action action--create">CREATE ACCOUNT</div>
</section>

</body>
</html>
```